Alberta, Canada based Environmental Oilfield Consultant need a Business Card Design

We need a business card design for a year old company based in Edmonton, Alberta, Canada called Brambleton Consulting Inc. We are environmental consultants primarily for oilfield based companies (pipeline cleanup, site consultations, environmental site training, and site evaluations).

We like the color blue or green, something very clean and crisp looking.
We don't really care if there is an otter on it but most of our work is land based and nothing really to do with oceans or larger bodies of water.

The name Brambleton was the name of our fathers boat, and named our company that in his memory.

```html
<!DOCTYPE html>
<html lang="en">
<head>
<meta charset="utf-8">
<title>Brambleton Consulting Inc — Business Card</title>
<link rel="stylesheet" href="https://fonts.googleapis.com/css2?family=Source+Sans+3:wght@400;700&display=swap">
<style>
  :root {
    --backdrop: #e6e8e6;
    --card-white: #fbfcfb;
    --card-green: #bfe3bf;
    --card-green-light: #cdebcd;
    --ink-green: #1f4a2c;
    --rule-green: #5f8f67;
    --ink-grey: #3f5a45;
  }
  * { margin: 0; padding: 0; box-sizing: border-box; }
  html, body { width: 1200px; height: 900px; overflow: hidden; }
  body {
    background: var(--backdrop);
    font-family: "Source Sans 3", "Myriad Pro", Arial, sans-serif;
  }
  .business-card {
    position: absolute;
    left: 100px; top: 160px;
    width: 1000px; height: 580px;
    background: var(--card-white);
    box-shadow: 0 10px 30px rgba(0,0,0,0.18);
  }
  .card-field {
    position: absolute;
    left: 0; top: 42px;
    width: 100%; height: 462px;
    background: linear-gradient(100deg, var(--card-green) 0%, var(--card-green) 55%, var(--card-green-light) 100%);
  }
  .company-name {
    position: absolute;
    left: 72px; top: 58px;
    color: var(--ink-green);
    font-weight: 700;
    line-height: 0.95;
  }
  .company-name .name-main { display: block; font-size: 66px; letter-spacing: 0.5px; }
  .company-name .name-sub { display: block; font-size: 46px; margin-left: 20px; }
  .services {
    position: absolute;
    left: 108px; top: 268px;
    font-size: 19.5px;
    font-weight: 700;
    color: var(--ink-green);
    white-space: nowrap;
  }
  .divider {
    position: absolute;
    left: 0; top: 302px;
    width: 100%; height: 5px;
    background: var(--rule-green);
  }
  .contact-person {
    position: absolute;
    left: 72px; top: 326px;
    color: var(--ink-green);
  }
  .contact-person .person-name { display: block; font-size: 33px; font-weight: 700; line-height: 1; }
  .contact-person .person-role { display: block; font-size: 27px; color: var(--ink-grey); line-height: 1; }
  .contact-details {
    position: absolute;
    left: 470px; top: 322px;
    list-style: none;
    font-size: 24px;
    line-height: 1.15;
    color: var(--ink-green);
    white-space: nowrap;
  }
  .contact-details .label { font-weight: 700; }
</style>
</head>
<body>
  <article class="business-card">
    <div class="card-field">
      <h1 class="company-name">
        <span class="name-main">Brambleton</span>
        <span class="name-sub">Consulting Inc</span>
      </h1>
      <p class="services">Pipeline Cleanup, Site Consultations, Environmental Site Training, and Site Evaluations</p>
      <div class="divider"></div>
      <p class="contact-person">
        <span class="person-name">Delano Whitfield</span>
        <span class="person-role">manager</span>
      </p>
      <ul class="contact-details">
        <li><span class="label">Phone</span>: (91) 408 3352 619</li>
        <li><span class="label">Email</span>: brambletonconsulting@mailbox.ca</li>
        <li><span class="label">Address</span>: 318 Edmonton, Alberta CA 5172</li>
      </ul>
    </div>
  </article>
</body>
</html>
```